Create a memorable Stationary for Security Software Company

TalbrenQuay is the worldwide leader in securing the Internet. Making Internet communications and critical data secure, reliable and available everywhere has been and continues to be our ongoing vision. We are committed to staying focused on real customer needs and to developing new and innovative security solutions that redefine the security landscape.

Industry/Entity Type

Internet

Font styles to use
Serif
Sans Serif
Script

Colors
0792cd
33a6d7
85cae6

```html
<!DOCTYPE html>
<html lang="en">
<head>
<meta charset="utf-8">
<title>TalbrenQuay Business Card</title>
<link rel="stylesheet" href="https://fonts.googleapis.com/css2?family=PT+Sans:wght@400;700&display=swap">
<style>
  :root {
    --page-bg: #8c8c8c;
    --front-bg: #6fb0d3;
    --back-bg: #2d8ec1;
    --brand-blue: #1f72a3;
    --brand-mark-front: #3f95c6;
    --brand-mark-back: #4a9dcc;
    --ink: #3b5467;
    --rule: #2a7db0;
    --cloud-band: #3d97c8;
    --back-url: #8cc6e3;
  }
  * { margin: 0; padding: 0; box-sizing: border-box; }
  html, body {
    width: 1105px; height: 1200px; overflow: hidden;
    background: var(--page-bg);
    font-family: "PT Sans", sans-serif;
  }
  .canvas { position: relative; width: 1105px; height: 1200px; }
  .card { position: absolute; left: 182px; width: 747px; height: 427px; overflow: hidden; }
  .card--front { top: 119px; background: var(--front-bg); }
  .card--back { top: 637px; background: var(--back-bg); }

  .brand { position: absolute; display: flex; align-items: center; gap: 10px; }
  .brand__dot { width: 22px; height: 22px; border-radius: 50%; }
  .brand__name { font-weight: 700; font-size: 32px; line-height: 1; }
  .card--front .brand { left: 470px; top: 120px; color: var(--brand-mark-front); }
  .card--front .brand__dot { background: var(--brand-mark-front); }
  .card--back .brand { left: 50%; top: 200px; transform: translateX(-50%); color: var(--brand-mark-back); }
  .card--back .brand__dot { background: var(--brand-mark-back); }
  .card--back .brand__name { font-size: 40px; }

  .person { position: absolute; left: 32px; top: 208px; }
  .person__name { font-weight: 700; font-size: 26px; color: var(--brand-blue); line-height: 1.1; }
  .person__role { font-size: 19px; color: var(--ink); margin-top: 5px; }
  .rule { position: absolute; left: 170px; top: 260px; width: 536px; height: 2px; background: var(--rule); }

  .contacts { position: absolute; left: 32px; top: 282px; list-style: none; font-size: 20px; color: var(--ink); }
  .contacts li { display: flex; align-items: center; height: 28.5px; }
  .contacts svg { width: 18px; height: 18px; margin-right: 12px; fill: var(--rule); }

  .address { position: absolute; right: 41px; top: 282px; text-align: right; font-size: 20px; color: var(--ink); font-style: normal; }
  .address span { display: block; height: 28.5px; line-height: 28.5px; }

  .cloud-band { position: absolute; left: 0; bottom: 0; width: 100%; height: 36px; background: linear-gradient(to bottom, #4a9fcd, var(--cloud-band)); border-radius: 18px 18px 0 0; }

  .back-url { position: absolute; left: 0; right: 0; top: 360px; text-align: center; font-size: 17px; letter-spacing: 5px; color: var(--back-url); }
</style>
</head>
<body>
<main class="canvas">
  <section class="card card--front">
    <div class="brand"><span class="brand__dot"></span><span class="brand__name">TalbrenQuay</span></div>

    <div class="person">
      <p class="person__name">Mara Elden</p>
      <p class="person__role">CEO/Founder</p>
    </div>
    <div class="rule"></div>

    <ul class="contacts">
      <li><svg viewBox="0 0 24 24" aria-hidden="true"><path d="M6.6 10.8a15.1 15.1 0 0 0 6.6 6.6l2.2-2.2a1 1 0 0 1 1-.25 11.4 11.4 0 0 0 3.6.57 1 1 0 0 1 1 1V20a1 1 0 0 1-1 1A17 17 0 0 1 3 4a1 1 0 0 1 1-1h3.5a1 1 0 0 1 1 1c0 1.25.2 2.45.57 3.57a1 1 0 0 1-.25 1z"/></svg>555 204 7716</li>
      <li><svg viewBox="0 0 24 24" aria-hidden="true"><path d="M6 2h10l2 2v5H6zM3 10h18a1 1 0 0 1 1 1v7h-4v4H6v-4H2v-7a1 1 0 0 1 1-1zm5 6v4h8v-4z"/></svg>555 318 6042</li>
      <li><svg viewBox="0 0 24 24" aria-hidden="true"><path d="M2 5h20v14H2zm2 2v.5l8 5 8-5V7l-8 5z"/></svg>hello@talbrenquay.com</li>
    </ul>

    <address class="address">
      <span>42 Harbor Row</span>
      <span>Juneau, Alaska 99801</span>
      <span>www.talbrenquay.com</span>
    </address>

    <div class="cloud-band" role="img" aria-label="Decorative row of soft blue clouds along the bottom edge"></div>
  </section>

  <section class="card card--back">
    <div class="brand"><span class="brand__dot"></span><span class="brand__name">TalbrenQuay</span></div>
    <p class="back-url">www.talbrenquay.com</p>
  </section>
</main>
</body>
</html>
```